Modern Quillby Tree Care Website

I need a website for a full service Tree Care company. The company provides tree pruning, tree removal, tree preservation, emergency services, stump grinding, and emergency tree services.

Target Market(s)

Customers that need tree services

Industry/Entity Type

Landscaping, Tree Services

Coding

Coded - Design and coding required

Number of Pages Required

5+ page

Font styles to use
Sans Serif

Requirements
Must have
• Good clean design that showcases the services the company provides.
Nice to have
• Services page; contact form, blog, home page, about page

```html
<!DOCTYPE html>
<html lang="en">
<head>
<meta charset="utf-8">
<title>Quillby Tree Care</title>
<link href="https://fonts.googleapis.com/css2?family=Roboto+Slab:wght@400;500;600;700;800&display=swap" rel="stylesheet">
<style>
:root{
  --cream:#f5f6dc;
  --green:#7cb83a;
  --orange:#f9ae3a;
  --orange-text:#e0901c;
  --dark:#111;
  --ink:#1d1d1d;
  --muted:#555;
  --line:#d8d9b8;
  --white:#fff;
}
*{margin:0;padding:0;box-sizing:border-box}
html,body{width:1200px;height:3162px;overflow:hidden}
body{font-family:"Roboto Slab",serif;color:var(--ink);position:relative;background:var(--white)}
.abs{position:absolute}
section,header,footer{position:absolute;left:0;width:1200px;overflow:hidden}

.topbar{top:0;height:30px;background:var(--cream);font-size:10px;letter-spacing:1.5px;text-align:center;line-height:30px;color:#222}

.hero{top:30px;height:530px;background:linear-gradient(90deg,#16260f 0%,#2d4a1f 30%,#4a5c2e 50%,#3b4c25 70%,#2c3f1c 100%)}
.hero-photo{position:absolute;inset:0;background:radial-gradient(ellipse at 45% 85%,#7a4a3a 0%,rgba(122,74,58,0) 40%),radial-gradient(ellipse at 80% 70%,#5b4530 0%,rgba(91,69,48,0) 35%),linear-gradient(180deg,rgba(10,20,8,.6),rgba(10,20,8,.1) 30%,rgba(10,20,8,.3))}
.logo{left:150px;top:22px;display:flex;align-items:center;gap:10px;color:var(--white);font-weight:700;font-size:20px;line-height:1.05}
.logo-mark{width:34px;height:34px;background:var(--green)}
.nav{left:444px;top:26px;width:329px;height:40px;border-top:1px solid rgba(255,255,255,.7);border-bottom:1px solid rgba(255,255,255,.7);display:flex;justify-content:space-around;align-items:center;font-size:12px;color:var(--white)}
.nav .active{color:var(--orange);border-bottom:3px solid var(--orange);padding:10px 0 7px;margin-top:3px}
.phone-btn{left:900px;top:26px;width:150px;height:40px;border-radius:20px;background:var(--green);color:#111;font-size:12px;display:flex;align-items:center;justify-content:center;gap:8px}
.hero-circle{left:230px;top:135px;width:314px;height:314px;border-radius:50%;background:rgba(30,40,25,.45)}
.hero-title{left:150px;top:160px;width:474px;text-align:center;color:var(--white)}
.hero-title .script{color:var(--orange);font-size:48px;font-weight:700;line-height:1}
.hero-title .main{font-size:54px;font-weight:800;line-height:1.05}
.hero-title p{font-size:14px;margin-top:24px;line-height:1.25}
.btn{display:flex;align-items:center;justify-content:center;border-radius:20px;font-size:12px;color:#222}
.btn-orange{background:var(--orange)}
.btn-green{background:var(--green)}
.slides{left:1030px;top:232px;font-size:12px;font-weight:700;color:var(--white);line-height:22.5px;text-align:right}
.slides .on{color:var(--orange)}
.slides .on::before{content:"";display:inline-block;width:16px;height:1px;background:var(--orange);vertical-align:middle;margin-right:4px}

.intro{top:560px;height:519px;background:var(--cream)}
.intro h2{position:absolute;top:80px;width:100%;text-align:center;font-size:33px;font-weight:500;line-height:1.1}
.feature{top:231px;width:291px;height:191px;border:1px solid var(--line);border-radius:8px;text-align:center;padding:54px 36px 0}
.feature .icon{position:absolute;left:110px;top:-37px;width:71px;height:71px;border-radius:50%;border:1px solid var(--line);background:var(--cream);display:flex;align-items:center;justify-content:center}
.feature h3{color:var(--orange-text);font-weight:500;font-size:16px;margin-bottom:8px}
.feature p{font-size:12.5px;line-height:1.25;color:#333}

.about{top:1079px;height:614px;background:var(--white)}
.photo-canopy{left:150px;top:89px;width:376px;height:417px;background:radial-gradient(circle at 45% 85%,#f4f0b0 0%,rgba(244,240,176,0) 25%),linear-gradient(180deg,#8cc43c,#3f7d22 55%,#24501a)}
.accent-green{left:526px;top:111px;width:36px;height:80px;background:var(--green)}
.accent-orange{left:475px;top:455px;width:80px;height:80px;background:var(--orange)}
.photo-frame{left:423px;top:143px;width:240px;height:309px;background:var(--white);padding:8px;box-shadow:0 4px 14px rgba(0,0,0,.2)}
.photo-worker{width:100%;height:100%;background:linear-gradient(180deg,#2e3a2a,#5a4a3c 55%,#c0521f 85%,#3a2a20)}
.about-text{left:708px;top:158px;width:320px}
.about-text h2{font-size:32px;font-weight:500;margin-bottom:14px}
.about-text p{font-size:12.5px;line-height:1.3;color:#333;margin-bottom:15px}

.services{top:1693px;height:649px;background:var(--orange)}
.service{width:291px;height:244px;background:var(--white);border-radius:8px;text-align:center;padding:22px 40px 0}
.service svg{display:block;margin:0 auto 10px}
.service h3{font-size:15.5px;font-weight:500;margin-bottom:8px}
.service p{font-size:12.5px;line-height:1.25;color:#444}

.why{top:2342px;height:517px;background:var(--white)}
.why-band{left:758px;top:0;width:442px;height:517px;background:var(--green)}
.why h2{position:absolute;left:157px;top:130px;font-size:32px;font-weight:500}
.why ul{position:absolute;left:157px;top:188px;list-style:none;font-size:13px;color:#333}
.why li{height:27px;display:flex;align-items:center;gap:8px}
.bullet{width:12px;height:12px;border-radius:50%;background:var(--orange);position:relative}
.bullet::after{content:"";position:absolute;left:10px;top:5px;width:8px;height:2px;background:var(--orange)}
.why li span{margin-left:6px}
.why-frame{left:570px;top:71px;width:372px;height:375px;background:var(--white);padding:8px;box-shadow:0 4px 14px rgba(0,0,0,.2)}
.why-photo{width:100%;height:100%;background:linear-gradient(160deg,#b58a58,#4a5a78 45%,#c0b8a8 80%,#d0c4b0)}

.footer{top:2859px;height:303px;background:radial-gradient(ellipse at 50% 40%,#16241a,#060b08 70%);color:var(--white);text-align:center}
.socials{position:absolute;top:105px;left:0;width:100%;display:flex;justify-content:center;gap:5px}
.socials span{width:39px;height:39px;border-radius:50%;border:1px solid rgba(255,255,255,.8)}
.footer-nav{position:absolute;left:0;top:161px;width:100%;font-size:12.5px}
.footer-nav b{font-weight:400;margin:0 6px}
.copyright{position:absolute;left:0;top:182px;width:100%;font-size:12.5px}
</style>
</head>
<body>

<header class="topbar">PROIN SUSCIPIT ID DUI FRINGILLA ULTRICIES</header>

<section class="hero">
  <div class="hero-photo" role="img" aria-label="Arborist in hard hat cutting a fallen log with a chainsaw on a forest road"></div>
  <div class="abs logo"><span class="logo-mark"></span><span>Quillby<br>Tree Care</span></div>
  <nav class="abs nav"><span class="active">Home</span><span>About Us</span><span>Services</span><span>Contact</span><span>Blog</span></nav>
  <div class="abs phone-btn">
    <svg width="14" height="14" viewBox="0 0 24 24" fill="none" stroke="#111" stroke-width="2"><path d="M5 3h4l2 5-3 2a11 11 0 0 0 6 6l2-3 5 2v4a2 2 0 0 1-2 2A17 17 0 0 1 3 5a2 2 0 0 1 2-2z"/></svg>
    (555) 014-2739
  </div>
  <svg class="abs" style="left:190px;top:120px" width="400" height="380" stroke="rgba(255,255,255,.8)" stroke-width="1">
    <line x1="315" y1="85" x2="370" y2="30"/><line x1="330" y1="75" x2="390" y2="18"/>
    <line x1="0" y1="380" x2="60" y2="320"/><line x1="22" y1="375" x2="80" y2="318"/>
  </svg>
  <div class="abs hero-circle"></div>
  <div class="abs hero-title">
    <div class="script">Quillby</div>
    <div class="main">TREE CARE</div>
    <p>Nulla ut velit ipsum. Ut augue arcu, elementum non augue vel<br>efficitur commodo dolor.</p>
  </div>
  <div class="abs btn btn-orange" style="left:255px;top:366px;width:129px;height:36px">Read More</div>
  <div class="abs btn btn-green" style="left:389px;top:366px;width:129px;height:36px">Contact us</div>
  <div class="abs slides"><div class="on">01</div><div>02</div><div>03</div><div>04</div></div>
</section>

<section class="intro">
  <h2>Nullam non nisl eu lacus efficitur<br>gravida ut ac tellus.</h2>
  <div class="abs feature" style="left:151px">
    <div class="icon"><svg width="40" height="34" viewBox="0 0 40 34" fill="none" stroke="#222" stroke-width="1.5"><circle cx="8" cy="26" r="5"/><circle cx="20" cy="26" r="5"/><circle cx="32" cy="26" r="5"/><path d="M14 18l14-10M24 4l6 6"/></svg></div>
    <h3>SED PLACERAT</h3>
    <p>Nullam non nisl eu lacus efficitur gravida ut ac tellus. Suspendisse et ligula a metus sodales egestas at at mi.</p>
  </div>
  <div class="abs feature" style="left:455px">
    <div class="icon"><svg width="40" height="40" viewBox="0 0 40 40" fill="none" stroke="#222" stroke-width="1.5"><rect x="12" y="14" width="10" height="18"/><path d="M8 4l10 10M4 36h32"/><rect x="22" y="26" width="12" height="8"/></svg></div>
    <h3>EFFICITUR COMMODO</h3>
    <p>Vivamus dapibus lectus eu urna facilisis, vel ornare quam finibus. Aenean ut mauris felis. Nullam egestas, augue id.</p>
  </div>
  <div class="abs feature" style="left:760px">
    <div class="icon"><svg width="36" height="40" viewBox="0 0 36 40" fill="none" stroke="#222" stroke-width="1.5"><path d="M18 4a8 8 0 0 1 8 7 7 7 0 0 1 2 13H8a7 7 0 0 1 2-13 8 8 0 0 1 8-7z"/><path d="M18 24v14M12 38h12"/></svg></div>
    <h3>CURABITUR CONGUE ERAT</h3>
    <p>Nullam non nisl eu lacus efficitur gravida ut ac tellus. Suspendisse et ligula a metus sodales egestas at at mi.</p>
  </div>
</section>

<section class="about">
  <div class="abs accent-green"></div>
  <div class="abs accent-orange"></div>
  <div class="abs photo-canopy" role="img" aria-label="Looking up through a green forest canopy toward the sun"></div>
  <div class="abs photo-frame"><div class="photo-worker" role="img" aria-label="Worker with ear defenders operating an orange sawmill cutting a log"></div></div>
  <div class="abs about-text">
    <h2>Who We Are</h2>
    <p>At Quillby Tree Care, we are more than just a tree service company, we are stewards of your beautiful trees. With a passion deeply rooted in arboriculture, we embark on a mission to promote the health, beauty, and safety of your trees and landscapes.</p>
    <p>Whether it's expert tree trimming to enhance aesthetics, meticulous tree removal to mitigate hazards, or comprehensive tree health assessments to ensure safety, we approach each task with unwavering dedication and attention to detail.</p>
    <div class="btn btn-orange" style="width:129px;height:37px;margin-top:16px">Read More</div>
  </div>
</section>

<section class="services">
  <div class="abs service" style="left:150px;top:70px">
    <svg width="46" height="48" viewBox="0 0 46 48" fill="none" stroke="#222" stroke-width="1.5"><path d="M14 26a8 8 0 1 1 4-15 9 9 0 0 1 16 2 7 7 0 0 1-2 13z"/><path d="M18 26l-4 20M28 26l4 20M23 26v20M6 46h34"/></svg>
    <h3>TREE TRIMMING</h3>
    <p>Nullam libero turpis, sodales eu ante quis, varius placerat ipsum. Nam interdum ante semper turpis fermentum, et molestie mi condimentum. Mauris lobortis ex ut mauris pretium luctus vitae et est.</p>
  </div>
  <div class="abs service" style="left:455px;top:70px">
    <svg width="54" height="48" viewBox="0 0 54 48" fill="none" stroke="#222" stroke-width="1.5"><circle cx="22" cy="10" r="5"/><rect x="6" y="22" width="34" height="10" rx="2"/><rect x="40" y="20" width="10" height="14"/><path d="M4 40h40M8 46h30"/></svg>
    <h3>TREE REMOVAL</h3>
    <p>Nullam scelerisque, tortor congue venenatis pharetra, velit neque rhoncus lacus, ac pulvinar massa nibh ac odio. Ut dignissim, libero at tincidunt imperdiet,</p>
  </div>
  <div class="abs service" style="left:760px;top:70px">
    <svg width="50" height="48" viewBox="0 0 50 48" fill="none" stroke="#222" stroke-width="1.5"><path d="M25 2l10 14h-5l8 12H12l8-12h-5z"/><path d="M25 28v18M4 46h42"/><circle cx="10" cy="32" r="6"/><circle cx="40" cy="32" r="6"/></svg>
    <h3>TREE CLEARING</h3>
    <p>Nullam libero turpis, sodales eu ante quis, varius placerat ipsum. Nam interdum ante semper turpis fermentum, et molestie mi condimentum. Mauris lobortis ex ut mauris pretium luctus vitae et est.</p>
  </div>
  <div class="abs service" style="left:150px;top:329px">
    <svg width="44" height="48" viewBox="0 0 44 48" fill="none" stroke="#222" stroke-width="1.5"><path d="M22 4a10 10 0 0 1 10 8 8 8 0 0 1 0 16H12a8 8 0 0 1 0-16A10 10 0 0 1 22 4z"/><path d="M22 28v18M16 22l6 6 6-6"/></svg>
    <h3>TREE PRUNING</h3>
    <p>Nullam libero turpis, sodales eu ante quis, varius placerat ipsum. Nam interdum ante semper turpis fermentum, et molestie mi condimentum. Mauris lobortis ex ut mauris pretium luctus vitae et est.</p>
  </div>
  <div class="abs service" style="left:455px;top:329px">
    <svg width="50" height="48" viewBox="0 0 50 48" fill="none" stroke="#222" stroke-width="1.5"><path d="M10 34V20h14l6 10h12v4"/><path d="M20 20l6-14 6 4-4 10"/><circle cx="14" cy="38" r="5"/><circle cx="36" cy="38" r="5"/><path d="M2 46h46"/></svg>
    <h3>STUMP GRINDING</h3>
    <p>Nullam scelerisque, tortor congue venenatis pharetra, velit neque rhoncus lacus, ac pulvinar massa nibh ac odio. Ut dignissim, libero at tincidunt imperdiet,</p>
  </div>
  <div class="abs service" style="left:760px;top:329px">
    <svg width="48" height="48" viewBox="0 0 48 48" fill="none" stroke="#222" stroke-width="1.5"><circle cx="24" cy="24" r="20"/><path d="M10 10l28 28"/><path d="M20 14l4 16 4-16M18 32h12"/></svg>
    <h3>TREE PRESERVATION</h3>
    <p>Nullam libero turpis, sodales eu ante quis, varius placerat ipsum. Nam interdum ante semper turpis fermentum, et molestie mi condimentum. Mauris lobortis ex ut mauris pretium luctus vitae et est.</p>
  </div>
</section>

<section class="why">
  <div class="abs why-band"></div>
  <h2>Why Choose Us?</h2>
  <ul>
    <li><i class="bullet"></i><span>Licensed and Insured</span></li>
    <li><i class="bullet"></i><span>24-Hours Emergency Services</span></li>
    <li><i class="bullet"></i><span>Locally Owned &amp; Operated</span></li>
    <li><i class="bullet"></i><span>Professional Work</span></li>
    <li><i class="bullet"></i><span>Safety is Our No.1 Priority</span></li>
    <li><i class="bullet"></i><span>Free Estimates</span></li>
    <li><i class="bullet"></i><span>Licensed Arborist on Staff</span></li>
  </ul>
  <div class="abs why-frame"><div class="why-photo" role="img" aria-label="Carpenter in hard hat using an electric planer on a timber frame site"></div></div>
</section>

<footer class="footer">
  <div class="socials" aria-label="Social links"><span></span><span></span><span></span></div>
  <div class="footer-nav">Home<b>|</b>About Us<b>|</b>Services<b>|</b>Contact<b>|</b>Blog</div>
  <div class="copyright">Copyright © 2024 Quillby tree care. All rights reserved.</div>
</footer>

</body>
</html>
```